Briefkopf für Verwaltung im Taubertal
Zielgruppe
Die Verwaltungsgemeinschaft Wendelmark setzt sich aus den vier Kommunen zusammen: Stadt Wendelquell, Gemeinde Birkenmoosau, Gemeinde Ulmsteinach und Gemeinde Haselwendtrieb. Als kommunaler Ansprechpartner sprechen wir alle Bürgerinnen und Bürger an.
Aufgabenstellung
Das Logo der Verwaltungsgemeinschaft soll im Briefkopf abgebildet werden. Wesentliche Inhalte wie Adresse, Telefon, Mail, etc. sollen vorhanden sein. Der Briefkopf sollte nach Möglichkeit der DIN-Norm (DIN 5008) entsprechen und Falzmarken enthalten. Der Ausdruck erfolgt vorwiegend in Schwarz-Weiß, nur gelegentlich in Farbe. Daher soll der Briefkopf auch in Schwarz-Weiß Druck optisch ansprechbar wirken und zudem relativ wenig Tonerfarbe verbrauchen. Die Gestaltung soll sowohl neutral, seriös, als auch freundlich wirken.

```html
<!DOCTYPE html>
<html lang="de">
<head>
<meta charset="utf-8">
<title>Briefbogen Verwaltungsgemeinschaft Wendelmark</title>
<link rel="stylesheet" href="https://fonts.googleapis.com/css2?family=Open+Sans:wght@400;600;700&family=Inter:wght@300;500&display=swap">
<style>
  :root {
    --backdrop: #e4e4e4;
    --paper: #ffffff;
    --ink: #1d1d1b;
    --accent: #a8282a;
    --rule: #333333;
  }
  * { margin: 0; padding: 0; box-sizing: border-box; }
  html, body { width: 862px; height: 1200px; overflow: hidden; background: var(--backdrop); }
  body { position: relative; font-family: "Open Sans", sans-serif; color: var(--ink); }

  .sheet {
    position: absolute; left: 37px; top: 43px; width: 787px; height: 1113px;
    background: var(--paper); border: 1px solid var(--rule);
  }
  .sheet > * { position: absolute; }

  .brand { left: 63px; top: 45px; display: flex; align-items: center; gap: 18px; }
  .brand__mark { width: 62px; height: 62px; background: var(--accent); }
  .brand__name {
    font-family: "Open Sans", sans-serif; font-weight: 400; font-size: 17px;
    letter-spacing: 2.4px; text-transform: uppercase; line-height: 1.55; color: var(--ink);
  }

  .return-address {
    left: 83px; top: 178px; width: 300px; text-align: center;
    font-size: 8.5px; padding-bottom: 1px; border-bottom: 0.8px solid var(--rule);
  }

  .window-dot { width: 1.5px; height: 1.5px; background: var(--ink); top: 343px; }
  .window-dot--left { left: 75px; }
  .window-dot--right { left: 393px; }

  .fold-mark { left: 11px; width: 15px; height: 1px; background: var(--ink); }
  .fold-mark--upper { top: 392px; }
  .fold-mark--lower { top: 555px; }

  .sender {
    left: 544px; top: 61px; height: 217px; padding-left: 8px;
    border-left: 1px solid var(--accent); font-size: 10.3px; line-height: 14.5px;
  }
  .sender p { margin-top: 8px; }
  .sender p:first-child { margin-top: 12px; }
  .sender .sender__legal { font-weight: 700; }
  .sender .sender__refs { margin-top: 26px; }

  .date-line { left: 553px; top: 318px; font-size: 10.3px; }

  .footer {
    left: 39px; top: 1032px; width: 720px; height: 57px;
    font-family: "Inter", sans-serif; font-weight: 300; font-size: 8.3px; line-height: 10.8px;
  }
  .footer__col { position: absolute; top: 0; height: 57px; padding-left: 8px; border-left: 1px solid var(--accent); }
  .footer__col--plain { border-left: none; }
  .footer__col h2 { font-size: 8.3px; font-weight: 500; color: var(--accent); margin-top: 5px; }
  .footer__col--plain { padding-top: 15.8px; }
  .col-members { left: 0; }
  .col-web { left: 198px; }
  .col-bank { left: 386px; }
  .col-bank2 { left: 554px; }
</style>
</head>
<body>
  <main class="sheet">
    <div class="brand">
      <span class="brand__mark"></span>
      <div class="brand__name">Verwaltungsgemeinschaft<br>Wendelmark</div>
    </div>

    <div class="return-address">VGem Wendelmark · Lindenplatz 4 · 97999 Wendelmark</div>

    <span class="window-dot window-dot--left"></span>
    <span class="window-dot window-dot--right"></span>

    <span class="fold-mark fold-mark--upper"></span>
    <span class="fold-mark fold-mark--lower"></span>

    <aside class="sender">
      <p class="sender__legal">Körperschaft<br>des öffentlichen Rechts</p>
      <p>Lindenplatz 4<br>97999 Wendelmark</p>
      <p>Tel. 0 91 00 / 45 60-0<br>Fax 0 91 00 / 45 60-49<br>E-Mail: info@wendelmark-vg.de</p>
      <p class="sender__refs">Unser Zeichen:<br>Ihnen schreibt:<br>Tel.-Durchwahl:<br>E-Mail:</p>
    </aside>

    <div class="date-line">Wendelmark, den</div>

    <footer class="footer">
      <div class="footer__col col-members">
        <h2>Mitgliedsgemeinden:</h2>
        Stadt Wendelquell<br>Gemeinde Birkenmoosau<br>Gemeinde Ulmsteinach<br>Gemeinde Haselwendtrieb
      </div>
      <div class="footer__col col-web">
        <h2>Homepages:</h2>
        www.wendelquell.de<br>www.birkenmoosau.de<br>www.ulmsteinach.de<br>www.haselwendtrieb.de
      </div>
      <div class="footer__col col-bank">
        <h2>Bankverbindungen:</h2>
        Kreiskasse Talgrund<br>IBAN: DE00 1234 5678 0000 1111 22<br>BIC: TALGDEX1XXX
      </div>
      <div class="footer__col footer__col--plain col-bank2">
        Bürgerbank Ufertal<br>IBAN: DE00 8765 4321 0000 2222 33<br>BIC: BUBKDEX1XXX
      </div>
    </footer>
  </main>
</body>
</html>
```